Simple 1 page layout for quiet-harbor-tools.com

Visit http://quiet-harbor-tools.com

The site calculates ipv6 unique local addresses for free. The content will stay as it is. There's going to be Zorvix promoslots below the red box and at the bottom of the page.

The red box contains the most important information on this page. The users focus should go there immediately.

The contents below composition is also kind of important.

Reason: I'm very busy at the moment. I need more time for evaluation and feedback. Thanks for your contributions and your patience.

Target Market(s)

IT and networking people

Industry/Entity Type

Zorvix

Requirements
Must have
• I need all pieces nicely cut, so I only have to do HTML and CSS.

```html
<!DOCTYPE html>
<html lang="en">
<head>
<meta charset="utf-8">
<title>Unique Local IPv6 – local network address generator</title>
<link rel="stylesheet" href="https://fonts.googleapis.com/css2?family=Arimo:ital,wght@0,400;0,700;1,700&family=Open+Sans:wght@400;600;700&display=swap">
<style>
:root{
  --page-bg:#f3f2ea;
  --paper:#f7f7f6;
  --paper-edge:#dcdcd8;
  --band:#527a84;
  --band-dark:#3f646d;
  --title:#333a3d;
  --accent:#5bb3cc;
  --accent-text:#3a9cbf;
  --heading:#4a7585;
  --rule:#b8cdd4;
  --text:#2a2a2a;
  --muted:#555;
  --note-a:#3fa8d6;
  --note-b:#a7eef5;
  --lower-bg:#e6e6e4;
}
*{box-sizing:border-box;margin:0;padding:0}
html,body{width:857px;height:1200px;overflow:hidden}
body{background:var(--page-bg);position:relative;font-family:"Arimo",Arial,sans-serif;color:var(--text)}
.abs{position:absolute}
.sheet-back{left:58px;top:16px;width:760px;height:1100px;background:#ececea;transform:rotate(.6deg);box-shadow:0 1px 4px rgba(0,0,0,.15)}
.sheet-back.two{left:50px;top:28px;transform:rotate(-.4deg);background:#efefed}
.sheet{left:47px;top:35px;width:765px;height:1100px;background:var(--paper);box-shadow:0 2px 6px rgba(0,0,0,.2)}
.band{top:58px;height:64px;background:linear-gradient(var(--band),var(--band-dark));box-shadow:0 3px 4px rgba(0,0,0,.3);border-radius:3px}
.band.left{left:42px;width:232px}
.band.right{left:584px;width:234px}
.masthead{left:272px;top:35px;width:314px;height:92px;background:#fff;text-align:center;box-shadow:0 2px 4px rgba(0,0,0,.15)}
.masthead h1{font:700 25px/1 "Arimo",Arial,sans-serif;color:var(--title);margin-top:29px;letter-spacing:-.3px;transform:scaleX(.95)}
.masthead p{font:italic 700 19px/1 "Arimo",Arial,sans-serif;color:var(--accent);margin-top:10px}
.note{left:57px;top:148px;width:390px;height:214px;background:linear-gradient(160deg,var(--note-a) 0%,#62c2e4 55%,var(--note-b) 100%);box-shadow:3px 4px 6px rgba(0,0,0,.3);color:#fff;font-family:"Open Sans",Verdana,sans-serif;padding:17px 18px}
.note .range{font-weight:700;font-size:12.5px;letter-spacing:.6px}
.note .dash{border-top:2px dashed rgba(255,255,255,.7);margin:12px 0 8px}
.note .row{font-size:10px;font-weight:600;margin-bottom:8px;letter-spacing:.2px}
.note .row span{display:inline-block;width:112px}
.note .hint{font-size:10.5px;margin-top:10px;letter-spacing:.3px}
.curl{right:0;bottom:0}
.composition{left:475px;top:148px;width:329px;height:219px;border:2px solid var(--accent);background:#fafafa;padding:9px 6px;font-family:"Open Sans",Verdana,sans-serif;font-size:10px;color:#444;letter-spacing:.3px}
.composition h2{font-size:11px;font-weight:700;letter-spacing:.6px;margin-bottom:6px}
.composition pre{font-family:inherit;font-size:10px;line-height:19.5px;white-space:pre}
.composition dl{margin-top:16px;line-height:15px}
.composition dt{float:left;width:56px;clear:left}
.composition dt.strong{font-weight:700}
.divider{left:57px;width:748px;border-top:1px dashed #bbb}
.faq-title,.side-title{border-top:2px solid var(--rule);border-bottom:2px solid var(--rule);font-family:"Open Sans",Verdana,sans-serif;font-weight:600;color:var(--heading);font-size:13px;padding:4px 6px}
.faq-title{left:78px;top:409px;width:243px;letter-spacing:.5px}
.faq-list{left:86px;top:445px;list-style:none;font-family:"Open Sans",Verdana,sans-serif;font-size:10px;color:var(--muted)}
.faq-list li{height:21px;display:flex;align-items:flex-start;gap:13px}
.faq-list svg{flex:none;margin-top:1px}
.side-title{left:397px;top:409px;width:398px;font-size:13.5px}
.side{left:404px;top:446px;width:390px;font-family:"Open Sans",Verdana,sans-serif;font-size:9.5px;color:var(--muted);line-height:13px}
.side h3{color:var(--accent-text);font-size:10px;font-weight:700;margin:13px 0 10px}
.side dl{line-height:13.5px}
.side dt{float:left;width:55px;clear:left}
.lower{left:52px;top:627px;width:756px;height:508px;background:linear-gradient(#efefee,var(--lower-bg))}
.topic{position:absolute;left:22px;width:710px}
.topic h2{display:flex;align-items:center;gap:5px;font:700 12px/1 "Arimo",Arial,sans-serif;color:var(--heading);letter-spacing:.2px}
.topic h2::after{content:"";flex:1;border-top:2px solid #c2c7c9;margin-top:2px}
.topic p{font-size:9.4px;line-height:14px;margin-top:9px;color:#222}
.copyright{left:0;width:900px;top:1167px;text-align:center;font-size:9px;color:#333}
</style>
</head>
<body>
<div class="abs sheet-back"></div>
<div class="abs sheet-back two"></div>
<div class="abs sheet"></div>

<div class="abs band left"></div>
<div class="abs band right"></div>
<header class="abs masthead">
  <h1>Unique Local IPv6</h1>
  <p>local network address generator</p>
</header>

<section class="abs note">
  <div class="range">fdae:89d4:a873::/48</div>
  <div class="dash"></div>
  <div class="row"><span>1st 64-bit subnet</span>fdae:89d4:a873::/64</div>
  <div class="row"><span>last 64-bit subnet</span>&nbsp;&nbsp;&nbsp;&nbsp;fdae:89d4:a873:ffff::/64</div>
  <div class="hint">Just reload this page to get a new one</div>
  <svg class="abs curl" width="42" height="24" viewBox="0 0 42 24"><path d="M0 24 Q22 22 42 0 L42 24Z" fill="#f7f7f6"/><path d="M0 24 Q20 14 42 0 Q30 18 8 24Z" fill="#2c93bd"/></svg>
</section>

<section class="abs composition">
  <h2>Composition</h2>
<pre>| 7 bits |1|  40 bits   |  16 bits  |          64 bits           |
+--------+-+------------+-----------+----------------------------+
| Prefix |L| Global ID  | Subnet ID |    Interface ID     |
+--------+-+------------+-----------+----------------------------+</pre>
  <dl>
    <dt class="strong">Prefix</dt><dd><b>fc::/7</b></dd>
    <dt>Local (L)</dt><dd>1</dd>
    <dt>Global ID</dt><dd>ae89d4a873 changes every time you visit this page</dd>
    <dt>Subnet ID</dt><dd>0 - ffff use freely for your own IPv6 subnetting</dd>
    <dt>Interface ID</dt><dd>&nbsp;&nbsp;&nbsp;&nbsp;Your host address.</dd>
  </dl>
</section>

<div class="abs divider" style="top:385px"></div>

<h2 class="abs faq-title">F.A.Q.</h2>
<ul class="abs faq-list">
  <li><svg width="14" height="11" viewBox="0 0 14 11"><rect x=".5" y=".5" width="13" height="10" fill="none" stroke="#5bb3cc"/><path d="M3 5.5h7M7 2.5l3 3-3 3" fill="none" stroke="#5bb3cc" stroke-width="1.2"/></svg>What's a unique local address?</li>
  <li><svg width="14" height="11" viewBox="0 0 14 11"><rect x=".5" y=".5" width="13" height="10" fill="none" stroke="#5bb3cc"/><path d="M3 5.5h7M7 2.5l3 3-3 3" fill="none" stroke="#5bb3cc" stroke-width="1.2"/></svg>What's the use?</li>
  <li><svg width="14" height="11" viewBox="0 0 14 11"><rect x=".5" y=".5" width="13" height="10" fill="none" stroke="#5bb3cc"/><path d="M3 5.5h7M7 2.5l3 3-3 3" fill="none" stroke="#5bb3cc" stroke-width="1.2"/></svg>Why do they need to be unique?</li>
  <li><svg width="14" height="11" viewBox="0 0 14 11"><rect x=".5" y=".5" width="13" height="10" fill="none" stroke="#5bb3cc"/><path d="M3 5.5h7M7 2.5l3 3-3 3" fill="none" stroke="#5bb3cc" stroke-width="1.2"/></svg>Are they really globally unique?</li>
  <li><svg width="14" height="11" viewBox="0 0 14 11"><rect x=".5" y=".5" width="13" height="10" fill="none" stroke="#5bb3cc"/><path d="M3 5.5h7M7 2.5l3 3-3 3" fill="none" stroke="#5bb3cc" stroke-width="1.2"/></svg>Isn't there an easy way?</li>
  <li><svg width="14" height="11" viewBox="0 0 14 11"><rect x=".5" y=".5" width="13" height="10" fill="none" stroke="#5bb3cc"/><path d="M3 5.5h7M7 2.5l3 3-3 3" fill="none" stroke="#5bb3cc" stroke-width="1.2"/></svg>What is the subnet id?</li>
  <li><svg width="14" height="11" viewBox="0 0 14 11"><rect x=".5" y=".5" width="13" height="10" fill="none" stroke="#5bb3cc"/><path d="M3 5.5h7M7 2.5l3 3-3 3" fill="none" stroke="#5bb3cc" stroke-width="1.2"/></svg>Where can I get more information?</li>
  <li><svg width="14" height="11" viewBox="0 0 14 11"><rect x=".5" y=".5" width="13" height="10" fill="none" stroke="#5bb3cc"/><path d="M3 5.5h7M7 2.5l3 3-3 3" fill="none" stroke="#5bb3cc" stroke-width="1.2"/></svg>What's a unique local address?</li>
</ul>

<h2 class="abs side-title">What's a unique local address?</h2>
<section class="abs side">
  <p>IPv6 unique local addresses are similar to the IPv4 private address classes with one big difference: THE ARE UNIQUE.</p>
  <h3>IPv4 private addresses</h3>
  <dl>
    <dt>Class A</dt><dd>10.0.0.0/8</dd>
    <dt>Class B</dt><dd>172.16.0.0/12</dd>
    <dt>Class C</dt><dd>192.168.0.0/16</dd>
  </dl>
  <h3>IPv6 unique local addresses</h3>
  <p>fd::/48 - fd:ffff:ffff::/48</p>
</section>

<div class="abs divider" style="top:625px"></div>

<section class="abs lower">
  <article class="topic" style="top:21px">
    <h2>What's the use?</h2>
    <p>Local network addresses are used to make specific services only available for people and computers within your private network.<br>For example if your company runs an intranet website containing confidential information about products, sales, customers or what so ever. This information might be vital for your employees to do their jobs, but you definitely don't want to make this website available publicly.</p>
  </article>
  <article class="topic" style="top:106px">
    <h2>Why do they need to be unique?</h2>
    <p>Sometimes you want to join two or more private networks. A common example is when you connect your PC from your home network to your office network using a VPN. When both networks use the same private address range (e.g. 192.168.1.0/24) you only reach the office network during your VPN session as a result of a routing problem.</p>
  </article>
  <article class="topic" style="top:192px">
    <h2>Are they really globally unique?</h2>
    <p>The global id part of unique local addresses is a randomly generated 40-bit integer. So there's a small possibility that two networks on this planet use the same unique local address. But there's a very little likelihood that this is ever going to happen. PROBABILITY: 1:1099511627776 or ~0.000000000001</p>
  </article>
  <article class="topic" style="top:270px">
    <h2>Isn't there an easy way?</h2>
    <p>If you want to use a unique local network for your personal use or for testing only, no one bars you from using fd::/48, fd:abba::/48 or fd:1234::/48. But keep in mind there's are reason they have been made unique in the first place. And there's actually no good reason not to use a randomly generated address. How about that one on top of this page?</p>
  </article>
  <article class="topic" style="top:352px">
    <h2>What is the subnet id?</h2>
    <p>After the global id you have 16 bits for your subnetting. Use them at will.<br>If you don't have any subnetting plans right now, just start with 0000 (luckily you don't have to write that).</p>
  </article>
  <article class="topic" style="top:427px">
    <h2>Where can I get more information?</h2>
    <p>RFC 4193</p>
  </article>
</section>

<footer class="abs copyright">&copy; Copyright</footer>
</body>
</html>
```